Creative Businesss Card desgin!

Create a business card for our business Gleam window cleaning!
We are open to creative ideas as long as it maintains a professional image.

Target Market(s)

Small Commercial window cleaning clients including car dealerships, strata manager, cafe

Industry/Entity Type

Window Cleaning

Contact Information for Business Card

Daniel Prescott
General Manager
Gleam Window Cleaning

daniel@gleamservices.com.au
pane-care-southbank.com.au
Ph: 1800 GET GLEAM
Mob: 0437 582 061

Colors
fbed22
0392cd

Requirements
Should not have
• Stock window cleaning/ squeegee graphics

```html
<!DOCTYPE html>
<html lang="en">
<head>
<meta charset="utf-8">
<title>Gleam Window Cleaning – Business Card</title>
<link rel="stylesheet" href="https://fonts.googleapis.com/css2?family=Quicksand:wght@400;500;700&display=swap">
<style>
  :root {
    --page: #ffffff;
    --sky: #1692cf;
    --deep: #0e5686;
    --sun: #f5ea1a;
  }
  * { box-sizing: border-box; margin: 0; padding: 0; }
  html, body {
    width: 1200px; height: 1000px; overflow: hidden;
    background: var(--page);
  }
  .business-card {
    position: absolute; left: 75px; top: 200px;
    width: 1050px; height: 600px;
    background: var(--sky);
    overflow: hidden;
    font-family: "Quicksand", sans-serif;
    color: var(--sun);
  }
  .card-swoosh { position: absolute; inset: 0; width: 1050px; height: 600px; }
  .card-swoosh path { fill: var(--deep); }

  .holder { position: absolute; left: 37px; top: 30px; }
  .holder-name {
    font-weight: 700; font-size: 44px; line-height: 1; letter-spacing: 0.2px;
  }
  .holder-role {
    margin-top: 14px; font-weight: 400; font-size: 24px; line-height: 30px;
    width: 272px; padding-bottom: 10px;
    border-bottom: 1px solid var(--sun);
  }

  .brand-mark {
    position: absolute; right: 37px; top: 50px;
    text-align: right; font-weight: 700; line-height: 1;
  }
  .brand-name { font-size: 72px; letter-spacing: 2px; }
  .brand-tag { font-size: 23px; margin-top: 6px; letter-spacing: 0.3px; }

  .contact-list { position: absolute; left: 74px; top: 258px; list-style: none; }
  .contact-item {
    display: flex; align-items: center; height: 48px;
    font-size: 24px; font-weight: 400;
  }
  .contact-icon { width: 40px; height: 36px; margin-right: 59px; flex: none; }
  .contact-icon * { fill: none; stroke: var(--sun); stroke-width: 2.6; stroke-linejoin: round; }
  .contact-icon .solid { fill: var(--sun); stroke: none; }
</style>
</head>
<body>
  <section class="business-card">
    <svg class="card-swoosh" viewBox="0 0 1050 600" aria-hidden="true">
      <path d="M377,0 C470,130 700,270 1050,403 L1050,0 Z"/>
      <path d="M107,600 C350,545 700,525 1050,552 L1050,600 Z"/>
    </svg>

    <header class="holder">
      <h1 class="holder-name">Daniel Prescott</h1>
      <p class="holder-role">General Manager<br>Gleam Window Cleaning</p>
    </header>

    <div class="brand-mark">
      <div class="brand-name">GLEAM</div>
      <div class="brand-tag">WINDOW CLEANING</div>
    </div>

    <ul class="contact-list">
      <li class="contact-item">
        <svg class="contact-icon" viewBox="0 0 40 36" aria-hidden="true">
          <path class="solid" d="M4,12 C4,4 36,4 36,12 L36,15 L28,15 L28,11 L12,11 L12,15 L4,15 Z"/>
          <path class="solid" d="M13,14 L27,14 L34,24 L34,31 L6,31 L6,24 Z"/>
        </svg>
        <span>1800 GET GLEAM</span>
      </li>
      <li class="contact-item">
        <svg class="contact-icon" viewBox="0 0 40 36" aria-hidden="true">
          <rect x="12" y="2" width="16" height="32" rx="2"/>
          <line x1="12" y1="7" x2="28" y2="7"/>
          <line x1="12" y1="29" x2="28" y2="29"/>
        </svg>
        <span>0437 582 061</span>
      </li>
      <li class="contact-item">
        <svg class="contact-icon" viewBox="0 0 40 36" aria-hidden="true">
          <rect x="8" y="10" width="24" height="16"/>
          <polyline points="8,10 20,20 32,10"/>
        </svg>
        <span>daniel@gleamservices.com.au</span>
      </li>
      <li class="contact-item">
        <svg class="contact-icon" viewBox="0 0 40 36" aria-hidden="true">
          <circle cx="20" cy="18" r="12.5"/>
          <ellipse cx="20" cy="18" rx="5.5" ry="12.5"/>
          <line x1="20" y1="5.5" x2="20" y2="30.5"/>
          <line x1="7.5" y1="18" x2="32.5" y2="18"/>
          <line x1="9.5" y1="11.5" x2="30.5" y2="11.5"/>
          <line x1="9.5" y1="24.5" x2="30.5" y2="24.5"/>
        </svg>
        <span>pane-care-southbank.com.au</span>
      </li>
    </ul>
  </section>
</body>
</html>
```